Pull Up Banner - Recruitment Company

We would like a design for a pull up banner.

For context: we are a recruitment business. We specialise in helping people in healthcare industry to find jobs in Australia.

I have come up with several ideas and text for the banner. Feel free to use the following as you see appropriate:

- Our logo (see attached)
- 'Healthcare Recruitment Agency'
- Some sort of imagine / cartoon of medical professionals (ie. doctor, nurse, physiotherapist, speech pathologist). A cartoon is more friendly than committing to a photo
- 'Empowering your next career move'
- 'Discover tailored opportunities based on your career preferences'
- Dot points (allied health, nursing, medical imaging)
- Contact info at the bottom including our website (www.quellstaffing.com.au, our Instagram handle @quellstaffing, Mobile: XXXX XXX XXX. The title section for contact information could be 'Get in touch:'

Feel free to submit a couple of designs and we can merge aspects that look good on your designs and find the perfect fit.
Thank you
Updates

Hello,

Thank you for your initial submissions to this project. I appreciate the time you've invested.

After reviewing the first attempt, I'd like to share some feedback and initial observations:

- Professionalism and engagement: Is the overall appearance of the banner professional? It's crucial that we have a high-quality design as this will represent our business.

- Image selection: The image (whether cartoon or real people) appears quite generic. Please consider submitting the banner with a few different photos in the middle for us to choose from. Ensure the image is a good fit and not simply a generic stock photo.

- Contact section: Kindly remove the phone number; we no longer wish to include it on the banner. Instead, please include our website (www.quellstaffing.com.au) and Instagram handle (@quellstaffing).

- Color scheme: White, black, and red/pink are preferred, or alternatively, blue. However, please avoid incorporating too many different colors as it may detract from the professional appearance.

We will be printing the design on a banner and require it to look professional and engaging.

Thank you once again for your submissions. I hope the feedback provided above is helpful.

Warm regards,

Target Market(s)

Allied Health Australia

Font styles to use
Serif

Colors
0054AA
0677BA
7BADD7
CADEEF
E8F1F8
0094D4
00A9DD
6FCCEA
C7EBF8
E9F6FB
EB3D1F
EC4F4E
F09395
F8D3D4
FCEDEE

```html
<!DOCTYPE html>
<html lang="en">
<head>
<meta charset="utf-8">
<title>Quell Staffing – Healthcare Recruitment Pull Up Banner</title>
<link rel="stylesheet" href="https://fonts.googleapis.com/css2?family=Anton&family=Poppins:wght@500;600;700&display=swap">
<style>
  :root {
    --brand-blue: #2231c9;
    --ink: #0b0b0b;
    --paper: #ffffff;
    --footer-black: #1c1c1c;
    --backdrop: #e8e8e8;
    --art-light: #5b68e0;
  }
  * { margin: 0; padding: 0; box-sizing: border-box; }
  html, body {
    width: 1090px; height: 1200px; overflow: hidden;
    background: var(--backdrop);
  }
  .canvas { position: relative; width: 1090px; height: 1200px; }
  .banner {
    position: absolute; left: 307px; top: 18px;
    width: 517px; height: 1264px;
    background: var(--paper);
    transform: scale(0.92); transform-origin: top left;
    font-family: "Poppins", sans-serif;
    overflow: hidden;
  }
  .centered { position: absolute; left: 0; right: 0; text-align: center; }
  .brand-name {
    top: 56px; font-weight: 700; font-size: 34px; letter-spacing: 4px;
    color: var(--ink);
  }
  .headline { font-family: "Anton", sans-serif; font-size: 62px; line-height: 1; letter-spacing: 1.5px; }
  .headline--1 { top: 152px; color: var(--brand-blue); }
  .headline--2 { top: 216px; color: var(--ink); font-size: 63px; }
  .headline--3 { top: 281px; color: var(--brand-blue); }
  .dot-row { top: 352px; display: flex; justify-content: center; gap: 7px; }
  .dot-row span { width: 8px; height: 8px; border-radius: 50%; background: var(--ink); }
  .tagline { top: 373px; font-weight: 700; font-size: 20px; color: var(--brand-blue); letter-spacing: -0.2px; }
  .team-art {
    position: absolute; left: 48px; top: 452px; width: 420px; height: 265px;
    border-bottom: 2px solid var(--ink);
    background: radial-gradient(ellipse 200px 150px at 50% 62%, var(--brand-blue) 0 98%, transparent 100%),
                linear-gradient(var(--paper), var(--paper));
  }
  .team-art::after {
    content: ""; position: absolute; left: 10px; right: 10px; top: 10px; bottom: 0;
    background: linear-gradient(90deg, rgba(91,104,224,.55), rgba(120,200,190,.45), rgba(255,255,255,.5), rgba(60,170,160,.5));
    opacity: .55; border-radius: 40px 40px 0 0;
  }
  .kicker { top: 773px; font-weight: 500; font-size: 15px; letter-spacing: 2.6px; color: var(--ink); }
  .subhead { font-family: "Anton", sans-serif; font-size: 37px; line-height: 1; letter-spacing: 1px; }
  .subhead--1 { top: 792px; color: var(--ink); }
  .subhead--2 { top: 832px; color: var(--brand-blue); }
  .specialty-band { position: absolute; left: 0; top: 896px; width: 517px; height: 120px; }
  .band-edge { position: absolute; top: 0; width: 38px; height: 120px; background: var(--brand-blue); }
  .band-edge--left { left: 0; }
  .band-edge--right { right: 0; }
  .specialty {
    position: absolute; top: 0; width: 121px; height: 120px;
    border: 2px solid var(--brand-blue);
    display: flex; align-items: center; justify-content: center; text-align: center;
    font-weight: 500; font-size: 21px; line-height: 1.25; color: var(--ink);
  }
  .specialty--allied { left: 60px; }
  .specialty--nursing { left: 202px; }
  .specialty--medical { left: 340px; }
  .contact-footer {
    position: absolute; left: 0; top: 1029px; width: 517px; height: 208px;
    background: var(--footer-black); color: var(--paper);
  }
  .contact-title { top: 20px; font-family: "Anton", sans-serif; font-size: 38px; line-height: 1; color: var(--brand-blue); letter-spacing: 1px; }
  .contact-line { display: flex; align-items: center; justify-content: center; gap: 9px; }
  .contact-line--phone { top: 78px; font-family: "Anton", sans-serif; font-size: 30px; line-height: 1; letter-spacing: .5px; }
  .contact-line--web { top: 149px; font-weight: 600; font-size: 18px; }
  .contact-line--social { top: 180px; font-weight: 600; font-size: 18px; }
  .contact-line--web, .contact-line--social { transform: translateY(-30px); }
  .social-dot { width: 17px; height: 17px; border-radius: 50%; background: var(--brand-blue); }
</style>
</head>
<body>
<div class="canvas">
  <section class="banner">
    <div class="brand-name centered">QUELL STAFFING</div>

    <h1>
      <span class="headline headline--1 centered">HEALTHCARE</span>
      <span class="headline headline--2 centered">RECRUITMENT</span>
      <span class="headline headline--3 centered">AGENCY</span>
    </h1>
    <div class="dot-row centered"><span></span><span></span><span></span><span></span><span></span></div>
    <p class="tagline centered">Empowering your next career move</p>

    <div class="team-art" role="img" aria-label="Cartoon group of healthcare professionals in scrubs and white coats standing before a blue circle"></div>

    <p class="kicker centered">DISCOVER TAILORED OPPORTUNITIES</p>
    <h2>
      <span class="subhead subhead--1 centered">BASED ON YOUR</span>
      <span class="subhead subhead--2 centered">CAREER PREFERENCES</span>
    </h2>

    <div class="specialty-band">
      <div class="band-edge band-edge--left"></div>
      <div class="specialty specialty--allied">Allied<br>health</div>
      <div class="specialty specialty--nursing">Nursing</div>
      <div class="specialty specialty--medical">Medical</div>
      <div class="band-edge band-edge--right"></div>
    </div>

    <footer class="contact-footer">
      <h3 class="contact-title centered">GET IN TOUCH</h3>
      <div class="contact-line contact-line--phone centered">
        <svg width="28" height="28" viewBox="0 0 28 28" aria-hidden="true">
          <circle cx="14" cy="14" r="14" fill="var(--brand-blue)"/>
          <path d="M9.5 7.5c.8-.6 1.6-.4 2 .3l1.4 2.4c.4.7.2 1.4-.4 1.8l-.9.6c.7 1.6 2.1 3 3.7 3.8l.6-.9c.4-.6 1.1-.8 1.8-.4l2.4 1.4c.7.4.9 1.2.3 2l-1 1.2c-.7.8-1.9 1-3 .5-3.5-1.5-6.3-4.3-7.8-7.8-.5-1.1-.3-2.3.5-3z" fill="none" stroke="#fff" stroke-width="1.5"/>
        </svg>
        <span>9123 456 780</span>
      </div>
      <div class="contact-line contact-line--web centered">
        <svg width="20" height="20" viewBox="0 0 20 20" aria-hidden="true">
          <circle cx="10" cy="10" r="10" fill="var(--brand-blue)"/>
          <g fill="none" stroke="#fff" stroke-width="1">
            <circle cx="10" cy="10" r="6"/>
            <ellipse cx="10" cy="10" rx="2.6" ry="6"/>
            <path d="M4 10h12M5 7h10M5 13h10"/>
          </g>
        </svg>
        <span>www.quellstaffing.com.au</span>
      </div>
      <div class="contact-line contact-line--social centered">
        <span class="social-dot"></span>
        <span>@quellstaffing</span>
      </div>
    </footer>
  </section>
</div>
</body>
</html>
```